I need a great, modern, professional website for my paint contracting company, Ashbrook Coating Contractors, LLC. I have many good pix that can be used from jobs completed that would be attractive. We do commercial, residential and industrial jobs. I’m fully insured and licensed, including holding a General Contractor’s License as a Subcontractor. I know nothing about coding websites. I’ll have my assistant get on tomorrow and learn how to drop files. I’m not sure what files to send. This will be difficult at best, it being able to talk this through. Oh well. What’s next?

Target Market(s)

General Contractors

Industry/Entity Type

Paint Contracting

Coding

Coded - Design and coding required

Font styles to use
Sans Serif

Colors
00AB8E
00BBA5
67D7C9
C6EFE9
E9F9F6

Requirements
Must have
• Pix of completed jobs, bio, maybe testimonials from happy customers? ….
Nice to have
• I’d like it to have a modern appeal, but still have some warmth.
Should not have
• ??

```html
<!DOCTYPE html>
<html lang="en">
<head>
<meta charset="utf-8">
<title>Ashbrook Coating Contractors – Website Design Notes</title>
<link rel="stylesheet" href="https://fonts.googleapis.com/css2?family=Abril+Fatface&family=Inter:wght@400;500;600;700&family=Lato:wght@400;700&display=swap">
<style>
:root{
  --teal-deep:#00AB8E;
  --teal:#00BBA5;
  --teal-mid:#62D6C6;
  --teal-soft:#C4EEE8;
  --teal-pale:#E8F8F5;
  --note:#E0201B;
  --board:#F2F2F2;
  --ink:#2B2B2B;
  --body:#555;
  --footer:#3C3C3C;
  --white:#fff;
}
*{margin:0;padding:0;box-sizing:border-box}
html,body{width:1200px;height:4172px;overflow:hidden}
body{background:var(--board);font-family:"Inter",sans-serif;color:var(--ink);position:relative}
.abs{position:absolute}
.display{font-family:"Abril Fatface",serif;font-weight:400}

/* designer notes */
.intro{left:13px;top:14px;width:1180px;font-family:"Lato",sans-serif;font-size:15.5px;line-height:22px;color:#222;font-weight:700}
.intro .link{color:var(--note);font-weight:400;font-size:17px;margin-top:8px;display:block}
.intro .link span{margin-left:40px;font-weight:700}
.note{position:absolute;left:13px;width:200px;font-family:"Lato",sans-serif;font-size:14.5px;line-height:19.5px;color:var(--note)}
.arrows{position:absolute;left:0;top:0;pointer-events:none}

/* site */
.site{position:absolute;left:216px;top:102px;width:984px;height:4070px;background:var(--white);overflow:hidden}
.hero{position:absolute;left:0;top:0;width:984px;height:692px;background:linear-gradient(180deg,#8aa27a 0%,#c9d2c2 30%,#e8ebe4 55%,#6f8a5a 85%,#4d6b3c 100%)}
.hero-shade{position:absolute;inset:0;background:rgba(0,0,0,.12)}
.brand{position:absolute;left:50px;top:12px;color:var(--white);font-weight:700;font-size:19px;line-height:28px;letter-spacing:.3px}
.nav{position:absolute;top:26px;left:313px;display:flex;gap:32px;color:var(--white);font-size:17px}
.nav .phone{color:var(--teal-mid);margin-left:58px}
.pill{position:absolute;background:var(--teal-mid);color:var(--white);font-weight:600;font-size:13px;border-radius:30px;display:flex;align-items:center;justify-content:center;letter-spacing:.3px}
.hero-title{position:absolute;left:0;top:252px;width:984px;text-align:center;color:var(--white);font-size:68px;line-height:72px}

.intro-block{position:absolute;top:692px;left:0;width:984px;text-align:center}
.intro-block h2{font-size:38px;margin-top:72px}
.rule{width:68px;height:3px;background:var(--teal-mid);margin:14px auto 0}
.intro-block p{width:680px;margin:6px auto 0;font-size:17px;line-height:25px;color:var(--body)}

.services{position:absolute;top:1053px;left:0;width:984px;height:473px;background:var(--teal-pale)}
.svc{position:absolute;width:240px}
.svc h3{font-size:27px;margin-bottom:22px;color:var(--ink)}
.svc p{font-size:15px;line-height:23.8px;color:var(--body)}
.svc-icon{position:absolute}

.project-img{left:182px;top:1596px;width:618px;height:262px;border-radius:12px;background:linear-gradient(180deg,#9fc3e6 0%,#dfe8ef 40%,#f2f2f0 60%,#6f8f55 100%)}
.side-card{background:linear-gradient(180deg,#7fcfc3,#5ab8ac);border-radius:10px}
.project-title{left:182px;top:1867px;font-size:42px;line-height:45px}
.project-loc{left:182px;top:1960px;font-size:24px;color:#666}
.project-desc{left:182px;top:2002px;width:440px;font-size:15.5px;line-height:25px;color:var(--body)}
.circle{position:absolute;width:60px;height:60px;border-radius:50%;display:flex;align-items:center;justify-content:center}
.circle.grey{background:#888}
.circle.teal{background:var(--teal-mid)}

.owner{position:absolute;top:2215px;left:0;width:984px;height:505px;background:var(--teal-soft)}
.owner-photo{position:absolute;left:0;top:0;width:328px;height:505px;background:linear-gradient(160deg,#d8d6cf 0%,#a9aca4 45%,#5e6a58 100%)}
.owner-name{position:absolute;left:372px;top:48px;font-size:62px;line-height:68px;color:#262626}
.owner-name u{text-decoration-thickness:4px;text-underline-offset:6px}
.owner-bio{position:absolute;left:656px;top:56px;width:275px;font-size:15px;line-height:23.7px;color:#3a3a3a}
.owner-bio p+p{margin-top:23.7px}
.spaced{letter-spacing:4px;font-size:11px;color:#666}

.testi-head{left:50px;top:2773px;font-size:40px}
.testi-rule{left:50px;top:2843px;width:68px;height:3px;background:var(--teal-mid)}
.quote-mark{left:233px;top:2848px;width:46px;height:34px;background:var(--teal-soft);border-radius:4px}
.testi-title{left:239px;top:2842px;font-size:39px;line-height:50px}
.stars{left:240px;top:2902px;color:var(--teal-mid);font-size:19px;letter-spacing:1px}
.testi-text{left:240px;top:2927px;width:560px;font-size:16px;line-height:25px;color:var(--body)}
.testi-name{left:240px;top:3003px;font-size:16px;font-weight:600}
.ghost{color:#555;font-size:11px;line-height:16px}

.store{position:absolute;top:3235px;left:0;width:984px;height:629px}
.store-panel{position:absolute;left:0;top:0;width:490px;height:629px;background:var(--teal-mid);color:var(--white)}
.store-photo{position:absolute;left:490px;top:0;width:494px;height:629px;background:linear-gradient(180deg,#6b6f72 0%,#8d9195 35%,#4f6578 60%,#7a6b55 100%)}
.store-panel h2{position:absolute;left:44px;top:48px;font-size:60px;line-height:69px}
.store-panel h2 u{text-decoration-thickness:4px;text-underline-offset:5px}
.store-panel p{position:absolute;left:44px;top:330px;width:360px;font-size:15px;line-height:23.6px}
.store-panel .addr{position:absolute;left:44px;top:523px;font-size:11px;letter-spacing:4px;line-height:18px}

.footer{position:absolute;top:3864px;left:0;width:984px;height:206px;background:var(--footer);color:#bdbdbd}
.fcol{position:absolute;top:38px;font-size:12.5px;line-height:29px;text-transform:uppercase}
.fcol h4{color:var(--white);font-size:15.5px;font-weight:700;line-height:20px;margin-bottom:6px}
.fcontact{position:absolute;left:591px;top:75px;font-size:11.5px;line-height:19px;width:170px}
.fbrand{position:absolute;left:50px;top:38px;color:var(--white);font-weight:700;font-size:19px;line-height:30px}
.flicense{position:absolute;left:50px;top:150px;color:var(--white);font-size:10.5px;line-height:15px}
.social{position:absolute;left:771px;top:40px;display:flex;gap:12px}
.social span{width:18px;height:18px;border-radius:50%;background:var(--teal)}
.copy{position:absolute;left:771px;top:73px;font-size:10px;line-height:15px;color:#aaa}
</style>
</head>
<body>

<div class="intro abs">
  Just a few notes and comments about my design, to explain things a bit better and clearer. I'm available for any feedback or questions you may have.<br>
  nb. I grabbed all the photos from your social page to give examples, some of them are a bit pixelated for this reason, they can all be replaced.
  <span class="link">Type this link in to your internet browser on your computer and also on your cell phone to see the website in action: <span>https://ashbrook-coating.example.io/</span></span>
</div>

<div class="note" style="top:131px">Your logo will go here</div>
<div class="note" style="top:302px">By clicking on your telephone number, users will be given the option to call you diretly from their phone</div>
<div class="note" style="top:513px">This button takes users to the contact page where they can either send you a message or find your number and address so they can get in touch</div>
<div class="note" style="top:667px">This background will change through pictures of your work</div>
<div class="note" style="top:936px">Feel free to let me know any changes you would like made to the text as you know best what message you would like to convey to your customers and potential customers</div>
<div class="note" style="top:1803px">Here you can showcase some of your best jobs which you're most proud of</div>
<div class="note" style="top:2420px">Here I would put a photo of you along with a bit of a bio about you</div>
<div class="note" style="top:2966px">Here you can have a supply of customer reviews and testimonials regarding your services</div>

<main class="site">
  <section class="hero" role="img" aria-label="Photo of a freshly painted white porch with columns and garden">
    <div class="hero-shade"></div>
    <div class="brand">ASHBROOK<br>COATING LOGO</div>
    <nav class="nav"><span>About</span><span>Services</span><span>Projects</span><span class="phone">(555) 014 2290</span></nav>
    <div class="pill" style="left:787px;top:19px;width:126px;height:38px">GET A QUOTE</div>
    <h1 class="hero-title display">Residential, commercial<br>&amp; industrial painting</h1>
    <div class="pill" style="left:399px;top:432px;width:165px;height:35px">GET A FREE QUOTE</div>
  </section>

  <section class="intro-block">
    <h2 class="display">Since 1905</h2>
    <div class="rule"></div>
    <p>Here at Ashbrook Coating we've got you covered: big jobs, little jobs and everything in between. With decades of knowledge and experience, we maintain the country's highest-quality standards. We guide our clients through all the process to make sure that the vision and client's needs are met.</p>
  </section>

  <section class="services">
    <svg class="svc-icon" style="left:84px;top:70px" width="48" height="30" viewBox="0 0 48 30"><path d="M4 12 L24 4 L44 12 V26 H4 Z" fill="var(--teal)"/><rect x="10" y="16" width="6" height="5" fill="#fff"/><rect x="21" y="16" width="6" height="10" fill="#fff"/><rect x="32" y="16" width="6" height="5" fill="#fff"/></svg>
    <svg class="svc-icon" style="left:378px;top:62px" width="48" height="42" viewBox="0 0 48 42"><rect x="6" y="6" width="36" height="34" fill="var(--teal)"/><g fill="#fff"><rect x="11" y="11" width="6" height="5"/><rect x="21" y="11" width="6" height="5"/><rect x="31" y="11" width="6" height="5"/><rect x="11" y="21" width="6" height="5"/><rect x="21" y="21" width="6" height="5"/><rect x="31" y="21" width="6" height="5"/><rect x="20" y="31" width="8" height="9"/></g></svg>
    <svg class="svc-icon" style="left:673px;top:64px" width="48" height="36" viewBox="0 0 48 36"><path d="M4 14 L24 4 L44 14 V30 H4 Z" fill="var(--teal)"/><g stroke="#fff" stroke-width="2"><line x1="10" y1="18" x2="38" y2="18"/><line x1="10" y1="23" x2="38" y2="23"/></g></svg>
    <div class="svc" style="left:84px;top:219px"><h3 class="display">Residential</h3><p>There's nothing like a fresh coat of paint to enhance your home. Interior and exterior painting, weatherproofing and wallpaper plus much more.</p></div>
    <div class="svc" style="left:377px;top:196px"><h3 class="display">Commercial</h3><p>The appearance of a business is an important factor. If the building looks poorly maintained, it will negatively affect the impression of customers. A fresh lick of paint can change all that.</p></div>
    <div class="svc" style="left:672px;top:219px"><h3 class="display">Industrial</h3><p>We are not afraid to tackle any challenge at any industrial facility. We are fully insured and have a wealth of experience working in all environments.</p></div>
  </section>

  <div class="abs side-card" style="left:0;top:1683px;width:89px;height:209px" role="img" aria-label="Preview of another completed project"></div>
  <div class="abs side-card" style="left:892px;top:1683px;width:110px;height:180px" role="img" aria-label="Preview of another completed project"></div>
  <div class="abs project-img" role="img" aria-label="Photo of a two-storey white house with wraparound porches"></div>
  <h3 class="abs project-title display">ANTEBELLUM<br>HOME</h3>
  <div class="abs project-loc">Cedar Hollow, AL</div>
  <p class="abs project-desc">Newly painted home, with our premium exterior latex semi gloss it will last for at least 20 years.</p>
  <div class="pill" style="left:182px;top:2083px;width:146px;height:45px;box-shadow:0 6px 14px rgba(0,0,0,.12)">VIEW PROJECTS</div>
  <div class="circle grey" style="left:758px;top:2053px"><svg width="20" height="12" viewBox="0 0 20 12"><path d="M19 6H2M7 1L2 6l5 5" stroke="#fff" stroke-width="1.6" fill="none"/></svg></div>
  <div class="circle teal" style="left:825px;top:2053px"><svg width="20" height="12" viewBox="0 0 20 12"><path d="M1 6h17M13 1l5 5-5 5" stroke="#fff" stroke-width="1.6" fill="none"/></svg></div>

  <section class="owner">
    <div class="owner-photo" role="img" aria-label="Photo of the owner painting a wall"></div>
    <h2 class="owner-name display"><u>Owner</u><br>Dale<br>Whitford</h2>
    <div class="owner-bio">
      <p>Dale has been in charge at Ashbrook Coating for ... years. He's helped to build on the already outstanding reputation of the company by always striving to make improvements and better the service provided wherever possible.</p>
      <p>With his expertise and experience, you can feel safe in the knowledge that Dale and his carefully curated team of professionals will get the job done to the highest possible standard.</p>
    </div>
    <div class="abs spaced" style="left:372px;top:436px">ASHBROOK, ALABAMA</div>
  </section>

  <h2 class="abs testi-head display">Testimonials</h2>
  <div class="abs testi-rule"></div>
  <div class="abs display" style="left:-6px;top:2888px;font-size:27px">ence!</div>
  <div class="abs ghost" style="left:0;top:2928px">brook coaters<br>for our</div>
  <div class="abs quote-mark"></div>
  <h3 class="abs testi-title display">Professional Process</h3>
  <div class="abs stars">★★★★★</div>
  <p class="abs testi-text">We couldn't be happier with the end product. The Ashbrook coaters team has been the ideal partner in the repainting process for our backyard office shed.</p>
  <div class="abs testi-name">Ray Colton</div>
  <div class="abs display" style="left:946px;top:2888px;font-size:27px">Pr</div>
  <div class="abs" style="left:946px;top:2912px;color:var(--teal-mid);font-size:12px">★★★</div>
  <div class="abs ghost" style="left:946px;top:2932px">I still<br>took<br>profes<br>a qual<br><b>Ray</b></div>
  <div class="circle grey" style="left:773px;top:3102px;width:56px;height:56px"><svg width="18" height="12" viewBox="0 0 20 12"><path d="M19 6H2M7 1L2 6l5 5" stroke="#fff" stroke-width="1.6" fill="none"/></svg></div>
  <div class="circle grey" style="left:840px;top:3102px;width:56px;height:56px"><svg width="18" height="12" viewBox="0 0 20 12"><path d="M1 6h17M13 1l5 5-5 5" stroke="#fff" stroke-width="1.6" fill="none"/></svg></div>

  <section class="store">
    <div class="store-panel">
      <h2 class="display">Come Visit<br>us in<br><u>STORE</u></h2>
      <p>If you would prefer to discuss your project in person or if you are planning a DIY job yourself, we are happy to welcome you in to our store in Ashbrook. We stock only the highest quality painting material and we'd love to discuss whichever idea you have together!</p>
      <div class="addr">48 RIDGEWAY ROAD<br>ASHBROOK, AL<br>36010</div>
    </div>
    <div class="store-photo" role="img" aria-label="Photo of the paint store front with its sign above the entrance"></div>
  </section>

  <footer class="footer">
    <div class="fbrand">ASHBROOK<br>COATING LOGO</div>
    <div class="flicense">Fully Insured &amp; Licensed<br>General Contractor's License</div>
    <div class="fcol" style="left:230px"><h4>THE COMPANY</h4>About<br>Services<br>Projects<br>Contact</div>
    <div class="fcol" style="left:409px"><h4>INFORMATION</h4>Privacy Policy<br>Terms &amp; Conditions</div>
    <div class="fcol" style="left:591px"><h4>CONTACT US</h4></div>
    <div class="fcontact">EMAIL: info@ashbrookcoating.com<br><br>PHONE: (555) 014 2290<br><br>ADDRESS: 48 Ridgeway Road, Ashbrook, AL 36010</div>
    <div class="social"><span></span><span></span><span></span></div>
    <div class="copy">© 2023 Ashbrook Coating LLC</div>
  </footer>
</main>

<svg class="arrows" width="1200" height="4172" viewBox="0 0 1200 4172">
  <defs><marker id="head" markerWidth="8" markerHeight="8" refX="7" refY="4" orient="auto"><path d="M0 0L8 4L0 8Z" fill="#E0201B"/></marker></defs>
  <g stroke="#E0201B" stroke-width="1.6" marker-end="url(#head)">
    <line x1="180" y1="141" x2="250" y2="141"/>
    <line x1="191" y1="309" x2="842" y2="139"/>
    <line x1="200" y1="552" x2="602" y2="552"/>
    <line x1="180" y1="677" x2="250" y2="677"/>
    <line x1="182" y1="946" x2="370" y2="946"/>
    <line x1="182" y1="1813" x2="370" y2="1813"/>
    <line x1="182" y1="2430" x2="370" y2="2430"/>
    <line x1="182" y1="2976" x2="370" y2="2976"/>
  </g>
</svg>
</body>
</html>
```